"Corporate Site Design of Cloud Application Venture"(Wordpress Design Project)

This task is new corporate site design for start-up.
Our company name is "Brindova."
Brindova is a cloud service for users who want to bring their software and settings on multiple computers.
Current beta service page is http://demo.brindova.net . But, now it is not available.
We suggest sample sites below. But, we don't want to follow there. We need you to focus our logo and our company will serve stable service.
http://www.quorvahub.net/design/624957/wordpress-design-by-pelmarix
http://www.quorvahub.net/design/637866/wordpress-design-by-tk
http://www.quorvahub.net/design/613671
http://www.quorvahub.net/design/555672
http://www.quorvahub.net/design/538594
http://www.quorvahub.net/design/544859
http://www.tavinor.net/portfolio/glimbrek/
http://layoutmarsh.net/item/design-company-site/96308
http://www.yorbitstudio.net/images/corporate-dl-thumb.jpg
http://www.vendorquay.net/product-tp/110085749/web_site_design_company.html
(1)we have already had logo-design and please must use it (attached).
we have attached 2 files.
Essential : brindova.ai
voluntary : brindovaicon.ai
(2)Unfortunately, we have no idea now, so depend on you about color, lay-out and something, but we wish people feel deeply impressive when they get our website.
(3)Only if you want to use phrase of my service, please use “Where there is Brindova, there’s your workspace.” (if the English grammar is not correct, please modify it.)
(4)The final design should look modern and sophisticated.
(5)Must have these contents.
In header.
- logo and facebook page link.(http://www.friendlattice.net/brindova)
In Header Menu.
- Top Page (has several news release)
- "News Release" List and News Release Page
- "About Service"
- "About Us"
- "Contact"
And footter has several links.
ex. News release, about service, about us, contact, hiring and so on.

```html
<!DOCTYPE html>
<html lang="en">
<head>
<meta charset="utf-8">
<title>Brindova – Where there is Brindova, there’s your workspace.</title>
<link rel="stylesheet" href="https://fonts.googleapis.com/css2?family=PT+Sans:ital,wght@0,400;0,700;1,700&family=PT+Sans+Narrow:wght@400;700&display=swap">
<style>
:root{
  --navy:#0b3a78;
  --blue:#1d5fa8;
  --sky:#1f9ad6;
  --ink:#1a1a1a;
  --grey:#555;
  --line:#d9dde2;
  --panel:#f7f8f9;
  --red:#a30d12;
  --dark:#2b2d30;
  --darker:#1b1c1e;
  --white:#fff;
}
*{box-sizing:border-box;margin:0;padding:0}
html,body{width:1086px;height:1200px;overflow:hidden}
body{font-family:"PT Sans",Arial,sans-serif;color:var(--ink);background:#f4f5f6;position:relative}
.abs{position:absolute}
a{color:inherit;text-decoration:none}

/* header */
.site-header{position:absolute;left:0;top:0;width:1086px;height:79px;background:linear-gradient(#fff,#f1f2f3);border-bottom:3px solid var(--navy)}
.brand{left:179px;top:18px;display:flex;align-items:center;gap:10px}
.brand-dot{width:22px;height:22px;border-radius:50%;background:var(--sky)}
.brand-name{font-family:"PT Sans",sans-serif;font-weight:700;font-size:40px;color:var(--blue);letter-spacing:.5px}
.follow{left:757px;top:8px;display:flex;align-items:center;gap:5px}
.follow-label{font-style:italic;font-weight:700;font-size:14px;color:var(--navy);margin-right:6px}
.follow-dot{width:15px;height:15px;border-radius:50%;background:#c9d4e2;border:1px solid #aab}
.main-nav{left:468px;top:40px;display:flex}
.nav-item{font-family:"PT Sans Narrow",sans-serif}
.nav-item strong{display:block;font-size:16px;font-weight:700;color:var(--ink);text-transform:uppercase}
.nav-item span{display:block;font-size:10px;color:#555;font-family:"PT Sans",sans-serif}
.nav-item.is-current strong{color:var(--navy)}

/* hero */
.hero{position:absolute;left:0;top:79px;width:1086px;height:317px;background:radial-gradient(ellipse at 55% 50%,#ffffff 0%,#eef0f2 55%,#dfe3e7 100%)}
.hero-welcome{left:226px;top:36px;font-family:"PT Sans Narrow",sans-serif;font-weight:700;color:var(--navy);font-size:27px;line-height:1}
.hero-title{left:226px;top:64px;font-family:"PT Sans Narrow",sans-serif;font-weight:700;font-size:33px;color:var(--ink)}
.hero-tagline{left:366px;top:102px;font-family:"PT Sans Narrow",sans-serif;font-style:italic;font-weight:700;font-size:18px;line-height:23px;color:var(--blue);white-space:nowrap}
.hero-intro{left:228px;top:152px;width:140px;font-size:11.5px;line-height:14px}
.hero-more{left:276px;top:241px;font-weight:700;font-size:11.5px}
.app-preview{left:570px;top:35px;width:331px;height:248px;background:linear-gradient(135deg,#2a5fc0,#5d93e0 45%,#c8cdd4 46%,#eef0f2);border:4px solid #c9ccd0}

/* features */
.features-band{position:absolute;left:0;top:396px;width:1086px;height:43px;background:var(--navy);color:var(--white);text-align:center;font-family:"PT Sans Narrow",sans-serif;font-weight:700;font-size:24px;line-height:43px}
.features-band small{font-size:17px;color:#9fb4d1;font-weight:400}
.features{position:absolute;left:173px;top:440px;width:731px;height:188px;display:flex;background:#fff;box-shadow:0 2px 4px rgba(0,0,0,.25)}
.feature{position:relative;flex:1;background:linear-gradient(#f6f7f8,#e9ebed);border-right:2px solid #fff}
.feature:last-child{border-right:0}
.feature-title{position:absolute;top:15px;width:100%;text-align:center;font-family:"PT Sans Narrow",sans-serif;font-weight:700;font-size:23px;color:var(--navy)}
.feature-text{position:absolute;left:13px;top:55px;width:140px;font-size:12px;line-height:15px;color:var(--blue)}
.feature-art{position:absolute;right:14px;top:54px;width:76px;height:80px;border-radius:8px;background:linear-gradient(#cfd8e4,#9aaec6)}
.btn-more{position:absolute;right:12px;bottom:22px;width:80px;height:18px;border-radius:4px;background:linear-gradient(#3d86cf,#0d4f98);color:#fff;font-size:10px;font-weight:700;line-height:18px;padding-left:12px}
.btn-more::after{content:"›";position:absolute;right:4px;top:3px;width:12px;height:12px;border-radius:50%;background:#fff;color:var(--navy);font-size:11px;line-height:11px;text-align:center}

/* tabs */
.tabs-panel{position:absolute;left:174px;top:658px;width:502px;height:239px;background:#fff;border:1px solid var(--line);border-radius:4px;box-shadow:0 1px 3px rgba(0,0,0,.12)}
.tab{position:absolute;top:11px;font-size:14px;font-weight:700;color:var(--ink);line-height:36px}
.tab em{font-style:normal;color:var(--blue)}
.tab.is-active{left:12px;width:128px;height:36px;background:linear-gradient(#f0f0f0,#d8d8d8);font-weight:400;padding-left:22px}
.tab-sep{position:absolute;top:11px;width:1px;height:36px;background:var(--line)}
.tab-arrows{position:absolute;right:14px;top:14px;font-size:22px;font-weight:700;color:#333;letter-spacing:4px}
.tab-body{position:absolute;left:10px;top:50px;width:480px;height:178px;background:linear-gradient(#f3f4f5,#fff);border-radius:3px}
.tab-heading{position:absolute;left:25px;top:24px;font-size:19px;font-weight:700;color:var(--navy)}
.tab-text{position:absolute;left:26px;top:52px;width:220px;font-size:11.5px;line-height:17px;color:var(--grey)}
.tab-text span{display:block;color:var(--blue);margin-top:4px}
.btn-red{position:absolute;background:var(--red);color:#fff;font-weight:700;font-size:11px;text-align:center;border:1px solid #700}
.tab-photo{position:absolute;left:262px;top:24px;width:205px;height:133px;background:linear-gradient(135deg,#b9c6d4,#e8ecf0 55%,#7f96b0)}

/* news */
.news-panel{position:absolute;left:692px;top:658px;width:213px;height:239px;background:#fff;border:1px solid var(--line);border-radius:4px;box-shadow:0 1px 3px rgba(0,0,0,.12)}
.news-heading{position:absolute;left:12px;top:16px;font-size:14px;font-weight:700}
.news-heading em{font-style:normal;color:var(--blue)}
.news-item{position:absolute;left:18px;width:175px;height:59px;border-bottom:1px dashed #ccc;font-size:9px}
.news-meta{display:flex;justify-content:space-between;font-weight:700;margin-bottom:6px}
.news-item p{color:var(--blue);line-height:11px}
.news-panel .btn-more{right:8px;bottom:8px}

/* footer */
.site-footer{position:absolute;left:0;top:928px;width:1086px;height:231px;background:radial-gradient(ellipse at 50% 40%,#3a3c40,var(--dark) 70%,#222)}
.footer-heading{position:absolute;top:18px;font-weight:700;font-size:15.5px;color:var(--sky)}
.tweets{position:absolute;left:186px;top:43px;width:180px;height:176px;background:#e7e8e9;border-radius:12px;padding:7px 10px;font-size:10.5px;line-height:12px}
.tweets::before{content:"";position:absolute;left:96px;top:-14px;border:8px solid transparent;border-left:18px solid #e7e8e9;border-bottom:6px solid #e7e8e9}
.tweet{padding-bottom:4px}
.tweet + .tweet{border-top:1px solid var(--blue);padding-top:6px}
.tweet strong{font-weight:400;font-size:12px;line-height:13px}
.tweet-by{text-align:right;font-size:9px;font-weight:700;line-height:10px;margin-top:2px}
.tweet-by em{font-style:normal;color:var(--blue);display:block}
.link-grid{position:absolute;left:406px;top:44px;width:249px;display:grid;grid-template-columns:1fr 1fr;font-size:11px;color:#bfc2c6}
.link-grid span{height:31px;line-height:26px;border-bottom:1px solid #6d7075}
.field{position:absolute;left:698px;width:196px;height:25px;background:#26282b;border:1px solid #55585c;color:#c8cbcf;font-size:11px;padding:5px 8px}
.legal{position:absolute;left:0;top:1159px;width:1086px;height:41px;background:var(--darker);color:#9a9da1;font-size:9px;text-align:center;line-height:41px}
.legal strong{color:#d0d2d4}
</style>
</head>
<body>

<header class="site-header">
  <a class="brand abs" href="#"><span class="brand-dot"></span><span class="brand-name">brindova</span></a>
  <div class="follow abs">
    <span class="follow-label">Follow Us:</span>
    <span class="follow-dot"></span><span class="follow-dot"></span><span class="follow-dot"></span><span class="follow-dot"></span><span class="follow-dot"></span>
  </div>
  <nav class="main-nav abs">
    <a class="nav-item is-current" style="width:70px"><strong>Home</strong><span>Take me home</span></a>
    <a class="nav-item" style="width:109px"><strong>News Release</strong><span>Our Latest News</span></a>
    <a class="nav-item" style="width:112px"><strong>About Service</strong><span>Range of Our Services</span></a>
    <a class="nav-item" style="width:85px"><strong>About Us</strong><span>Know our History</span></a>
    <a class="nav-item"><strong>Contact Us</strong><span>Get in touch</span></a>
  </nav>
</header>

<section class="hero">
  <div class="hero-welcome abs">Welcome to</div>
  <h1 class="hero-title abs">Brindova Website</h1>
  <p class="hero-tagline abs">Where there<br>is Brindova,<br>there’s your workspace.</p>
  <p class="hero-intro abs">Lorem Ipsum is simply dummy text of the printing and typesetting industry. Lorem Ipsum has been the industry's standard dummy text ever since the 1500s.</p>
  <a class="hero-more abs">Read More</a>
  <div class="app-preview abs" role="img" aria-label="Screenshot of the Brindova desktop app window with a drag and drop area to sync applications"></div>
</section>

<div class="features-band">-- features of Brindova <small>Inc</small> --</div>

<section class="features">
  <article class="feature">
    <h2 class="feature-title">-- Brindova --</h2>
    <p class="feature-text">Brindova is a software business to synchronize application via Internet with the proprietary software virtual technology.</p>
    <div class="feature-art" role="img" aria-label="Laptop, tablet and phone connected to a cloud"></div>
    <a class="btn-more">Read More</a>
  </article>
  <article class="feature">
    <h2 class="feature-title">-- R &amp; D --</h2>
    <p class="feature-text">We do research and development of new business and receive a patent in advance for our future core business.</p>
    <div class="feature-art" role="img" aria-label="Globe covered with research keywords" style="border-radius:50%;background:radial-gradient(#f4f4f4,#a9acb0)"></div>
    <a class="btn-more">Read More</a>
  </article>
  <article class="feature">
    <h2 class="feature-title">-- investment --</h2>
    <p class="feature-text">We are operating a strategic business plan by investing into companies of high affinity. Also we are investing for raising funds and profit to our business.</p>
    <div class="feature-art" role="img" aria-label="Figure with umbrella beside a green dollar sign" style="background:linear-gradient(#3a3a3a 30%,#e8e8e8 31%,#6fb04a)"></div>
    <a class="btn-more">Read More</a>
  </article>
</section>

<section class="tabs-panel">
  <div class="tab is-active">Who <em>We Are</em></div>
  <div class="tab-sep" style="left:156px"></div>
  <div class="tab" style="left:174px">Why <em>Choose Us</em></div>
  <div class="tab-sep" style="left:300px"></div>
  <div class="tab" style="left:314px">Our <em>Services</em></div>
  <div class="tab-arrows">‹›</div>
  <div class="tab-body">
    <h2 class="tab-heading">WHO WE ARE</h2>
    <p class="tab-text">Lorem ipsum dolor sit amet, consectetur adipiscing elit. Mauris posuere, enim sed sodales pretium, nisl libero varius tellus, ut <span>pellentesque lorem quis laoreet. Aenean</span></p>
    <a class="btn-red" style="left:26px;top:144px;width:78px;height:21px;line-height:19px">Read More</a>
    <div class="tab-photo" role="img" aria-label="Business team meeting with a presenter pointing at a board"></div>
  </div>
</section>

<aside class="news-panel">
  <h2 class="news-heading">Recent <em>News Release</em></h2>
  <div class="news-item" style="top:44px"><div class="news-meta"><span>@ 14-03-2012</span><span>By: Mr. Velan</span></div><p>Lorem Ipsum is simply dummy text of the printing and typesetting industry....</p></div>
  <div class="news-item" style="top:103px"><div class="news-meta"><span>@ 14-03-2012</span><span>By: Mr. Velan</span></div><p>Lorem Ipsum is simply dummy text of the printing and typesetting industry....</p></div>
  <div class="news-item" style="top:162px;border-bottom:0"><div class="news-meta"><span>@ 14-03-2012</span><span>By: Mr. Velan</span></div><p>Lorem Ipsum is simply dummy text of the printing and typesetting industry....</p></div>
  <a class="btn-more">Read More</a>
</aside>

<footer class="site-footer">
  <h3 class="footer-heading" style="left:186px">Latest Tweets</h3>
  <div class="tweets">
    <div class="tweet"><strong>Title Here:</strong><br>Lorem Ipsum is simply dummy text of the printing and typesetting industry.<div class="tweet-by"><em>Mr. Lorem Ipsum</em>@ 9:40 AM Feb 2</div></div>
    <div class="tweet"><strong>Title Here:</strong><br>Lorem Ipsum is simply dummy text of the printing and typesetting industry.<div class="tweet-by"><em>Mr. Lorem Ipsum</em>@ 9:40 AM Feb 2</div></div>
  </div>

  <h3 class="footer-heading" style="left:406px">Link Heading</h3>
  <div class="link-grid">
    <span>- Lorem Ipsum is simply</span><span>- Lorem Ipsum is simply</span>
    <span>- Lorem Ipsum is simply</span><span>- Lorem Ipsum is simply</span>
    <span>- Lorem Ipsum is simply</span><span>- Lorem Ipsum is simply</span>
    <span>- Lorem Ipsum is simply</span><span>- Lorem Ipsum is simply</span>
    <span style="border:0">- Lorem Ipsum is simply</span><span style="border:0">- Lorem Ipsum is simply</span>
  </div>

  <h3 class="footer-heading" style="left:698px">Contact Us</h3>
  <div class="field" style="top:48px">Name</div>
  <div class="field" style="top:77px">Email</div>
  <div class="field" style="top:106px;height:78px">Message</div>
  <a class="btn-red" style="left:699px;top:188px;width:62px;height:22px;line-height:20px">Submit</a>
</footer>

<div class="legal">Copyright © 2012 Brindova®. All Rights Reserved &nbsp;|&nbsp; Phone: +123 456 7890, Fax: +123 456 789. Email @: <strong>info@brindova.net</strong></div>

</body>
</html>
```